Thornbury Equity Corporation
Thank you everyone for all your designs and your help and your willingness to provide changes. This process has been so amazing thanks to all of you. The desins were so strong it was almost impossible to make a decision. Hopefully we will work with you all in the future!
Extended the contest a few days, still time to add if you have any new ideas (not that we don't have a lot of great ideas to choose from already!) because you never know which it will be!
Thank you again everyone, we've asked some of you for some additions and we are working on a short list. Three of us are working on this project so not all choices have been graded with stars, so you are all possibly still in the running ;-).
Hopefully we can have a winner picked early next week.
Cheers
Wow amazing! Thank you everyone, digging thru them all today.
Good Morning Everyone,
Thank you so much for taking part in our next contest. However, we need besides the business cards some stationary so it would be lovely if you would be able to submit that along with the business cards.
Cheers,

```html
<!DOCTYPE html>
<html lang="en">
<head>
<meta charset="utf-8">
<title>Thornbury Equity Corporation — Stationery</title>
<link href="https://fonts.googleapis.com/css2?family=Cinzel:wght@700&family=Open+Sans:wght@400;600&display=swap" rel="stylesheet">
<style>
  :root {
    --navy: #1d2470;
    --navy-deep: #121752;
    --ink: #111114;
    --paper: #ffffff;
    --backdrop: #e3cfa9;
    --label: #5a4a30;
    --faint: #e6e6ea;
    --grey-text: #6b6b75;
  }
  * { box-sizing: border-box; margin: 0; padding: 0; }
  html, body { width: 1200px; height: 446px; overflow: hidden; }
  body {
    position: relative;
    background: var(--backdrop);
    font-family: "Open Sans", sans-serif;
  }
  .sheet, .card, .envelope, .envelope-back {
    position: absolute;
    background: var(--paper);
    box-shadow: 0 2px 5px rgba(60,40,10,.35);
    overflow: hidden;
  }
  .brand {
    position: absolute;
    display: flex;
    align-items: center;
    gap: 4px;
    font-family: "Cinzel", serif;
    font-weight: 700;
    color: var(--navy);
    white-space: nowrap;
    line-height: 1;
  }
  .brand-dot {
    border-radius: 50%;
    background: var(--navy);
    flex: none;
  }
  .brand-card {
    gap: 2px;
    font-size: 5px;
    line-height: 1.15;
    white-space: normal;
    width: 58px;
  }
  .brand-card .brand-dot { width: 5px; height: 5px; }
  .label {
    position: absolute;
    font-size: 6px;
    letter-spacing: .3px;
    color: var(--label);
    text-transform: uppercase;
  }
  .swoosh { position: absolute; left: 0; bottom: 0; width: 100%; }
  .seal {
    position: absolute;
    border-radius: 50%;
    border: 6px solid var(--faint);
  }
  .contact {
    position: absolute;
    font-size: 4.5px;
    line-height: 1.5;
    color: var(--grey-text);
  }

  /* business cards */
  .card-front { left: 12px; top: 158px; width: 68px; height: 42px; }
  .card-back { left: 12px; top: 230px; width: 68px; height: 42px; }

  /* letterheads */
  .letterhead-one { left: 168px; top: 19px; width: 281px; height: 333px; }
  .letterhead-two { left: 473px; top: 19px; width: 279px; height: 333px; }

  /* envelope backs */
  .envelope-back { left: 870px; width: 260px; }
  .envelope-back .flap { position: absolute; left: 0; top: 0; width: 100%; height: 100%; }
  .back-navy { top: 10px; height: 76px; }
  .back-black { top: 96px; height: 66px; }
  .back-white { top: 172px; height: 82px; }

  /* envelope front */
  .envelope { left: 792px; top: 262px; width: 338px; height: 142px; }
</style>
</head>
<body>

  <span class="label" style="left:12px; top:140px;">Corporate Identity</span>

  <!-- business card front -->
  <div class="card card-front">
    <div class="brand brand-card" style="left:4px; top:5px;">
      <span class="brand-dot"></span><span>Thornbury Equity Corporation</span>
    </div>
    <div class="contact" style="left:5px; top:20px; font-size:3.5px;">Jane Doe<br>Managing Director</div>
    <svg class="swoosh" viewBox="0 0 100 20" preserveAspectRatio="none" height="10">
      <path d="M0 10 Q50 0 100 10 L100 20 L0 20 Z" fill="var(--navy)"/>
    </svg>
  </div>
  <span class="label" style="left:12px; top:204px;">Business Card Front</span>

  <!-- business card back -->
  <div class="card card-back">
    <div class="brand brand-card" style="left:6px; top:15px;">
      <span class="brand-dot"></span><span>Thornbury Equity Corporation</span>
    </div>
  </div>
  <span class="label" style="left:12px; top:276px;">Business Card Back</span>

  <!-- letterhead option 1 -->
  <div class="sheet letterhead-one">
    <div class="brand" style="left:14px; top:22px; font-size:9px;">
      <span class="brand-dot" style="width:8px; height:8px;"></span>Thornbury Equity Corporation
    </div>
    <div class="contact" style="left:200px; top:14px;">
      Tel 555 014 2290<br>Fax 555 014 2291<br>info@thornburyequity.com<br>www.thornburyequity.com
    </div>
    <div class="seal" style="left:72px; top:120px; width:140px; height:140px;"></div>
    <svg class="swoosh" viewBox="0 0 100 20" preserveAspectRatio="none" height="26">
      <path d="M0 8 Q50 -2 100 8" fill="none" stroke="var(--navy)" stroke-width=".4"/>
      <path d="M0 12 Q50 2 100 12 L100 20 L0 20 Z" fill="var(--navy)"/>
    </svg>
  </div>
  <span class="label" style="left:270px; top:358px;">Letter Head Option 1</span>

  <!-- letterhead option 2 -->
  <div class="sheet letterhead-two">
    <div class="brand" style="left:60px; top:22px; font-size:9px;">
      <span class="brand-dot" style="width:8px; height:8px;"></span>Thornbury Equity Corporation
    </div>
    <div class="seal" style="left:70px; top:120px; width:140px; height:140px;"></div>
    <div class="contact" style="left:26px; bottom:30px; white-space:nowrap;">
      200 Harbour Street, Suite 4, Easton, ON &nbsp;|&nbsp; Tel 555 014 2290 &nbsp;|&nbsp; www.thornburyequity.com
    </div>
    <svg class="swoosh" viewBox="0 0 100 20" preserveAspectRatio="none" height="26">
      <path d="M0 8 Q50 -2 100 8" fill="none" stroke="var(--navy)" stroke-width=".4"/>
      <path d="M0 12 Q50 2 100 12 L100 20 L0 20 Z" fill="var(--navy)"/>
    </svg>
  </div>
  <span class="label" style="left:575px; top:358px;">Letter Head Option 2</span>

  <!-- envelope backs -->
  <div class="envelope-back back-navy">
    <svg class="flap" viewBox="0 0 260 76" preserveAspectRatio="none">
      <path d="M0 0 H260 V28 Q130 66 0 28 Z" fill="var(--navy)"/>
      <circle cx="130" cy="34" r="7" fill="var(--paper)"/>
    </svg>
  </div>
  <div class="envelope-back back-black">
    <svg class="flap" viewBox="0 0 260 66" preserveAspectRatio="none">
      <path d="M0 0 H260 V26 Q130 62 0 26 Z" fill="var(--ink)"/>
      <circle cx="130" cy="32" r="7" fill="var(--paper)"/>
    </svg>
  </div>
  <div class="envelope-back back-white">
    <svg class="flap" viewBox="0 0 260 82" preserveAspectRatio="none">
      <path d="M0 0 H260 V30 Q130 68 0 30" fill="none" stroke="#c9c9cf" stroke-width="1"/>
      <circle cx="130" cy="36" r="7" fill="var(--navy)"/>
    </svg>
  </div>

  <!-- envelope front -->
  <div class="envelope">
    <div class="brand" style="left:10px; top:10px; font-size:9px;">
      <span class="brand-dot" style="width:8px; height:8px;"></span>Thornbury Equity Corporation
    </div>
    <svg class="swoosh" viewBox="0 0 100 20" preserveAspectRatio="none" height="24">
      <path d="M0 8 Q50 -2 100 8" fill="none" stroke="var(--navy)" stroke-width=".4"/>
      <path d="M0 12 Q50 2 100 12 L100 20 L0 20 Z" fill="var(--navy)"/>
    </svg>
  </div>
  <span class="label" style="left:935px; top:410px;">Envelope Option 1</span>

</body>
</html>
```